Wordpress Design Project

i bought a wordpress template, bought my domain and my hosting package. i need someone to pull it all together and design my website and get it up and running.

i have the content, the logos, the look and feel of my design and i will provide these to you. I will need the headings on the theme to change and there will need to be some customization, including the the Social Icons-would need new icons creating similar in look to the existing ones, and then some minor code changes to have a new option appear in the Theme Options panel (ie; Enter your Linkedin username: , rss feed)

i will want one of the pull down tabs to have

I will want the wordpress theme to be SEO optimized. The site is optimized with SEO in mind, but also want the free WordPress plugin called Rankwise Suite added and any others that you feel are compelling.

the theme is: http://layoutbazaar.example/item/prism-adaptive-clean-html5-theme/4827365?WT.ac=category_item&WT.seg_1=category_item&WT.z_author=DovikStellan

The following design brief gives more information:

- Business Name? Bright Harbor Collective, LLC dba Bright Harbor Collective

- What do you do? Build coalitions for social good

- How many pages do you need designed and code? see template

- What is your industry? social entrepreneurship

- Describe the target audience for your website design? general public

- What 3 things would you like to communicate to your audience through your website design? 1. we are progressive 2. We use the power and merits of Capitalism to transcend poverty, preserve our planet and harness the collective power of the people 3. we are change makers
- How is your company different from your competitors? i invented a business model that will accomplish the above.

- What website design styles do you like? see theme
- What colors do you want to see in your website design? see theme and see my logo/business card.
- What colors do you NOT want to see in your website design? want to stay consistent with current design.
- What adjectives should best describe your website design? modern, artsy, engaging
- What content must be included in the website design? i will provide that later

ill also want you to provide what a process for working with me, including timeline.

the headers will be 

Home
Who We Are
What We Do
Our Projects
Blog
Latest News
Contact Us

What I am looking for is a mock up of the home page to mimic the prism wordpress theme.  the first project we will be working on is bringing vertical urban farming/manufactured in buildings - in disadvantaged neighborhoods. 

i have uploaded an executive summary so you know what we do as a company.

I would like to see what images you come up with and how you will incorporate the logo / existing look and feel into the home page.  this will give me a good idea of whom I would like to hire for the job.  this way you are not spending too much time and I can spot what i like immediately.

please also include your capacity to code according to what is required in the prism theme.  i want to make sure you are not just a graphic designer as I need the backend and some coding capacity.

thanks.

Target Market(s)

general public / corporate america

Industry/Entity Type

Progressive

Requirements
Must have
• even though this is a corporate website, i want the site to be artsy. i like the grey/black and white look and feel of what the template looks like and i want orange as the highlight color.

i will be adding color photos and video to the site. which i do not have yet.

i uploaded the logo and watermark, along with the front and back of my business card so that we remain consistent.

the watermark is used on my stationary and email template.

i will also need the control panel turned over to me when finished so that i may manage going forward.

i would also like to have an ongoing relationship with the web designer as I will be creating other sites as my business takes off.

```html
<!DOCTYPE html>
<html lang="en">
<head>
<meta charset="utf-8">
<title>Bright Harbor Collective — Home</title>
<link rel="stylesheet" href="https://fonts.googleapis.com/css2?family=Roboto+Condensed:ital,wght@0,700;1,700;1,800&family=Arimo:wght@400;700&display=swap">
<style>
  :root {
    --orange: #e8581d;
    --ink: #222222;
    --text: #4a4a4a;
    --nav-bg: #2a2b2c;
    --nav-edge: #9a9a9a;
    --header-bg: #e6e7e8;
    --band-bg: #e4e5e6;
    --icon-blue: #3a97c9;
    --white: #ffffff;
    --rule: #bdbdbd;
  }
  * { margin: 0; padding: 0; box-sizing: border-box; }
  html, body { width: 1080px; height: 1200px; overflow: hidden; background: var(--white); }
  body { position: relative; font-family: "Arimo", Arial, sans-serif; color: var(--text); }

  .site-header {
    position: absolute; left: 0; top: 0; width: 1080px; height: 216px;
    background: var(--header-bg);
    background-image: repeating-linear-gradient(45deg, rgba(255,255,255,.25) 0 2px, transparent 2px 4px);
  }
  .brand { position: absolute; left: 30px; top: 118px; display: flex; align-items: center; gap: 12px; }
  .brand-dot { width: 34px; height: 34px; border-radius: 50%; background: var(--orange); }
  .brand-name { font-family: "Arimo", Arial, sans-serif; font-weight: 700; font-size: 27px; color: #3c3c3c; }

  .social { position: absolute; top: 24px; right: 42px; display: flex; gap: 21px; }
  .social-circle { width: 37px; height: 37px; border-radius: 50%; border: 2px solid var(--icon-blue); }

  .phone { position: absolute; left: 843px; top: 120px; display: flex; align-items: center; gap: 14px; }
  .phone-number { font-family: "Arimo", Arial, sans-serif; font-weight: 700; font-size: 24px; color: var(--orange); letter-spacing: .3px; }

  .main-nav {
    position: absolute; left: 0; top: 216px; width: 1080px; height: 54px;
    background: var(--nav-bg); border-top: 4px solid var(--nav-edge);
  }
  .main-nav a {
    position: absolute; top: 17px; font-size: 13.5px; color: var(--white);
    text-decoration: none; text-transform: uppercase; letter-spacing: .2px;
  }
  .main-nav a.is-current { color: var(--orange); }

  .hero-slider { position: absolute; left: 14px; top: 273px; width: 1052px; height: 345px; }
  .hero-image {
    width: 100%; height: 100%;
    background: linear-gradient(100deg, #1c2c33 0%, #3d5560 22%, #8b979c 42%, #b9c4cc 60%, #4b4a44 75%, #9aa4a8 100%);
  }
  .slider-arrow {
    position: absolute; top: 141px; width: 37px; height: 64px; background: #111;
    display: flex; align-items: center; justify-content: center;
  }
  .slider-arrow.prev { left: 0; }
  .slider-arrow.next { right: 0; }

  .tagline-band {
    position: absolute; left: 0; top: 623px; width: 1080px; height: 82px;
    background: var(--band-bg);
    border-bottom: 3px solid #d5d5d5;
  }
  .tagline {
    position: absolute; left: 0; width: 100%; top: 22px; text-align: center;
    font-family: "Roboto Condensed", "Arial Narrow", sans-serif; font-style: italic; font-weight: 800;
    font-size: 30px; color: var(--orange); text-transform: uppercase; letter-spacing: .4px;
  }

  .about-head { position: absolute; left: 40px; top: 751px; height: 68px; display: flex; align-items: center; }
  .about-title { font-family: "Arimo", Arial, sans-serif; font-weight: 700; font-size: 21px; color: var(--ink); width: 201px; }
  .about-divider { width: 1px; height: 68px; background: var(--rule); }
  .about-name { margin-left: 27px; font-size: 17px; color: var(--orange); }

  .about-copy { position: absolute; left: 31px; top: 868px; width: 808px; font-size: 12.4px; line-height: 17.6px; color: var(--text); }
  .about-copy p { margin-bottom: 17.6px; }

  .founder-photo {
    position: absolute; left: 870px; top: 867px; width: 192px; height: 256px;
    background: #e9e9e9; padding: 7px;
  }
  .founder-photo-fill {
    width: 100%; height: 100%;
    background: linear-gradient(160deg, #6b6256 0%, #c8a778 40%, #8a7358 70%, #2d2a27 100%);
  }
</style>
</head>
<body>
  <header class="site-header">
    <div class="brand">
      <span class="brand-dot"></span>
      <span class="brand-name">Bright Harbor Collective</span>
    </div>
    <div class="social">
      <span class="social-circle" aria-label="Social link"></span>
      <span class="social-circle" aria-label="Social link"></span>
    </div>
    <div class="phone">
      <svg width="16" height="32" viewBox="0 0 16 32" aria-hidden="true">
        <rect x="1" y="1" width="14" height="30" rx="2" fill="none" stroke="#3a97c9" stroke-width="2"/>
        <rect x="4" y="5" width="8" height="11" fill="#3a97c9"/>
        <rect x="4" y="19" width="8" height="8" fill="#3a97c9" opacity=".6"/>
      </svg>
      <span class="phone-number">917 555 0142</span>
    </div>
  </header>

  <nav class="main-nav">
    <a class="is-current" href="#" style="left:42px">Home</a>
    <a href="#" style="left:133px">Who We Are</a>
    <a href="#" style="left:269px">What We Do</a>
    <a href="#" style="left:407px">Our Projects</a>
    <a href="#" style="left:558px">Blog</a>
    <a href="#" style="left:646px">Latest News</a>
    <a href="#" style="left:788px">Contact Us</a>
  </nav>

  <section class="hero-slider">
    <div class="hero-image" role="img" aria-label="City street photo: subway station sign, a businessman in motion and a bronze bull statue among skyscrapers"></div>
    <span class="slider-arrow prev">
      <svg width="12" height="18" viewBox="0 0 12 18" aria-hidden="true"><path d="M10 2 L3 9 L10 16" fill="none" stroke="#fff" stroke-width="3"/></svg>
    </span>
    <span class="slider-arrow next">
      <svg width="12" height="18" viewBox="0 0 12 18" aria-hidden="true"><path d="M2 2 L9 9 L2 16" fill="none" stroke="#fff" stroke-width="3"/></svg>
    </span>
  </section>

  <section class="tagline-band">
    <h2 class="tagline">Building Coalition for Social Good</h2>
  </section>

  <section class="about">
    <div class="about-head">
      <h3 class="about-title">ABOUT FOUNDER</h3>
      <span class="about-divider"></span>
      <span class="about-name">Dana Whitfield, Founder &amp; Social Enterpreneur</span>
    </div>
    <div class="about-copy">
      <p>I am deeply troubled by the paradigm that we have created in our systems/culture. Discrimination and sexism continue to plague humanity. I know that the best and brightest do not always have equal access and opportunity</p>
      <p>We are told that "all men are created equal, that they are endowed by their Creator with certain inalienable Rights that among these are Life, Liberty and the pursuit of Happiness." The American Dream is the birthright of its citizens; an undeniable freedom which includes the opportunity for prosperity and success regardless of class, race, religion or gender. Yet, the American Dream is becoming nearly unattainable for 98%.</p>
      <p>I had achieved financial/professional success; yet, I had a deep desire to contribute to society. I explored how I could best integrate my values/societal concerns with my expertise. Patterns began to emerge. It was as if my life in every capacity was aligning for a single purpose. I was profoundly inspired. I invented a model to resolve a once unthinkable challenge – combining the prosperity of business with the economic empowerment of the disadvantaged and the sustainability of the planet.</p>
      <p>I launched my company, Bright Harbor Collective. I use the power and merits of Capitalism to transcend poverty and to preserve our planet. I am proud to call myself a Social Entrepreneur. Social Entrepreneurs act as the change agents for society, seizing opportunities others miss. We improve systems, invent new approaches, and create solutions to change society for the better.</p>
    </div>
    <div class="founder-photo">
      <div class="founder-photo-fill" role="img" aria-label="Portrait photo of the founder"></div>
    </div>
  </section>
</body>
</html>
```